New Business Card Design Project VORASTI-Italy

we are VORASTI-Italy
our company in the market for 3 years we are luxury cosmetic company and its about time for a facelift :)
i will like to have elegant luxurious and unique business card
that will give the person that get it a unique, luxurious and elegant impression
I'm VERY OPEN FOR NEW IDEAS , even duo i add a few files of things that i see on line and i like them

i add my logo as well
my website is VORASTI.COM
(if you would like to see the main style that we have)

Target Market(s)

adult that have money :)

Industry/Entity Type

Business

Contact Information for Business Card

Name - Paul Vorasti
Position - CEO and CO Founder
address - 4817 E Larkdale
telephone - 555-384-1962
email - paul@vorasti.com
fax - 555-384-1962
website - VORASTI.COM

Colors
000000
959595
fbee3e
ffffff

Requirements
Must have
• big logo in GOLD color
• elegant look
• impressive
Nice to have
• not must but maybe classy pattern background
• not must but maybe emblem
• maybe clear plastic business card
Should not have
• colors
• images

```html
<!DOCTYPE html>
<html lang="en">
<head>
<meta charset="utf-8">
<title>VORASTI Italy – Business Card</title>
<link rel="stylesheet" href="https://fonts.googleapis.com/css2?family=Cormorant+Garamond:wght@400;500;600&display=swap">
<style>
  :root {
    --ink: #000000;
    --card-black: #0b0b0b;
    --gold: #c9a543;
    --gold-light: #e6cf78;
    --gold-deep: #9a8d3e;
    --yellow: #fbee3e;
    --pale-gold: #eadb86;
    --white: #ffffff;
    --grey: #959595;
    --backdrop: #e8e5e0;
    --serif: "Cormorant Garamond", Georgia, serif;
  }
  * { box-sizing: border-box; margin: 0; padding: 0; }
  html, body { width: 1200px; height: 1200px; overflow: hidden; }
  body {
    background: var(--backdrop);
    font-family: var(--serif);
    display: flex;
    flex-direction: column;
    align-items: center;
    justify-content: center;
    gap: 60px;
  }
  .card {
    position: relative;
    width: 840px;
    height: 480px;
    overflow: hidden;
    box-shadow: 0 6px 18px rgba(0,0,0,.18);
  }

  /* Front */
  .card--front { background: var(--card-black); }
  .front__brand {
    position: absolute;
    left: 60px; top: 70px;
    width: 320px;
    display: flex; flex-direction: column; align-items: center;
  }
  .brand-dot {
    width: 96px; height: 96px;
    border-radius: 50%;
    background: var(--gold);
    margin-bottom: 22px;
  }
  .brand-name {
    font-weight: 500;
    font-size: 58px;
    letter-spacing: 3px;
    line-height: 1;
  }
  .brand-sub {
    font-weight: 500;
    font-size: 18px;
    letter-spacing: 3px;
    margin-top: 8px;
  }
  .card--front .brand-name,
  .card--front .brand-sub { color: var(--gold); }

  .front__divider {
    position: absolute;
    left: 410px; top: 60px;
    width: 1px; height: 330px;
    background: var(--gold);
  }
  .front__contact {
    position: absolute;
    left: 445px; top: 70px;
    color: var(--white);
  }
  .person-name {
    color: var(--gold-light);
    font-size: 36px;
    font-weight: 500;
    letter-spacing: 1px;
    line-height: 1.1;
  }
  .person-title {
    font-size: 17px;
    margin-top: 4px;
  }
  .contact-rule {
    width: 330px; height: 1px;
    background: var(--gold);
    margin: 12px 0 22px -35px;
  }
  .contact-list { list-style: none; font-size: 18px; line-height: 1.5; }
  .contact-list + .contact-list { margin-top: 16px; }
  .contact-list .label { color: var(--gold); display: inline-block; width: 28px; }

  .front__band {
    position: absolute; left: 0; right: 0; bottom: 0;
    height: 34px;
  }

  /* Back */
  .card--back {
    background: radial-gradient(ellipse at 48% 40%, #efe089 0%, #d1bd62 40%, var(--gold-deep) 100%);
    display: flex; flex-direction: column; align-items: center; justify-content: center;
  }
  .card--back .brand-dot { background: var(--ink); width: 84px; height: 84px; margin-bottom: 20px; }
  .card--back .brand-name,
  .card--back .brand-sub { color: var(--ink); }
  .card--back .brand-name { font-size: 54px; }
  .back__address {
    margin-top: 14px;
    font-size: 18px;
    color: #2a2715;
  }
</style>
</head>
<body>

  <section class="card card--front" aria-label="Business card front">
    <div class="front__brand">
      <div class="brand-dot"></div>
      <div class="brand-name">VORASTI</div>
      <div class="brand-sub">ITALY</div>
    </div>

    <div class="front__divider"></div>

    <div class="front__contact">
      <div class="person-name">PAUL VORASTI</div>
      <div class="person-title">CEO and CO Founder</div>
      <div class="contact-rule"></div>
      <ul class="contact-list">
        <li><span class="label">T :</span> 555-384-1962</li>
        <li><span class="label">F :</span> 555-384-1962</li>
      </ul>
      <ul class="contact-list">
        <li><span class="label">W :</span> www.vorasti.com</li>
        <li><span class="label">E :</span> paul@vorasti.com</li>
      </ul>
    </div>

    <svg class="front__band" viewBox="0 0 840 34" preserveAspectRatio="none" aria-hidden="true">
      <rect x="0" y="0" width="570" height="34" fill="#fbee3e"/>
      <rect x="570" y="0" width="270" height="34" fill="#eadb86"/>
      <polygon points="562,34 570,0 576,0 568,34" fill="#000000"/>
    </svg>
  </section>

  <section class="card card--back" aria-label="Business card back">
    <div class="brand-dot"></div>
    <div class="brand-name">VORASTI</div>
    <div class="brand-sub">ITALY</div>
    <div class="back__address">4817 E Larkdale</div>
  </section>

</body>
</html>
```